Social Media Banner Design - Professional Football (Soccer)

Require matching banners for use across social media platforms.

The final design should be provided in 3 variations to align with the dimension requirements of:
- Facebook
- Twitter
- Linkedin

And also be compatible across desktop and mobile devices.

We would also request provision of the raw file so that should dimension requirements change moving forward, or additional social media outlets provide the option for page banners, that these can be catered for accordingly.

Subject of the project is a Sports personality, aligned to their club.

The following are requirements of the final designs:
1. Include One (1) image of the subject. Various photos of subject provided (subject can be cropped out of larger photo for use in designs. Please note that if subject image contains logo of an organisation, this should be digitally edited out of the final design)
2. Include name of the subject (Dorian Halvorsen)
3. Include image of the club logo (provided)
4. Include name of the club (Tuvo Rembeka)
4. Colour scheme of banner. Primary colour = green; secondary colour = white; third colour blue (all pantone as per club logo provided)

Additional potential inclusions that may be referenced / included in banners - but not required. These should only be included if they do not may the overall design look messy or cramped.
1. Nickname of club ( N'Usimbe )
2. Club Location reference (Kenya)
3. Subject social media channels (Facebook = coachhalvorsen, Twitter = dorryhalvorsen, Instagram = coachhalvorsen)
4. Subject website address = www.dorryhalvorsen-example.com

Target Market(s)

Football Supporters, Sports Fans, Industry professionals

Industry/Entity Type

Football

Colors
59FF00
82FF00
B8FF75
E3FFCB
F4FFEA

Requirements
Must have
• 1. Include One (1) image of the subject. Various photos of subject provided (subject can be cropped out of larger photo for use in designs. Please note that if subject image contains logo of an organisation, this should be digitally edited out of the final design) 2. Include name of the subject (Dorian Halvorsen) 3. Include image of the club logo (provided) 4. Include name of the club (Tuvo Rembeka) 4. Colour scheme of banner. Primary colour = green; secondary colour = white; third colour blue (all pantone as per club logo provided)
Nice to have
• Additional potential inclusions that may be referenced / included in banners - but not required. These should only be included if they do not may the overall design look messy or cramped. 1. Nickname of club ( N'Usimbe ) 2. Club Location reference (Kenya) 3. Subject social media channels (Facebook = coachhalvorsen, Twitter = dorryhalvorsen, Instagram = coachhalvorsen) 4. Subject website address = www.dorryhalvorsen-example.com

```html
<!DOCTYPE html>
<html lang="en">
<head>
<meta charset="utf-8">
<title>Dorian Halvorsen – Social Banners</title>
<link href="https://fonts.googleapis.com/css2?family=Bebas+Neue&family=Montserrat:wght@400;700;800&display=swap" rel="stylesheet">
<style>
  :root{
    --sheet:#dcdcdc;
    --green-deep:#03602e;
    --green-mid:#077a42;
    --lime:#55f500;
    --white:#ffffff;
    --blue:#2b4c9e;
    --kit-top:#2a3142;
    --kit-bottom:#161a24;
    --label:#1a1a1a;
  }
  *{margin:0;padding:0;box-sizing:border-box}
  html,body{width:1016px;height:1200px;overflow:hidden;background:var(--sheet)}
  .sheet{position:relative;width:1016px;height:1200px}
  .platform-label{
    position:absolute;left:0;width:1046px;text-align:center;
    font-family:"Montserrat",sans-serif;font-weight:400;font-size:23px;
    letter-spacing:1px;color:var(--label);
  }
  .banner{position:absolute;overflow:hidden;background:var(--green-deep);
    box-shadow:0 8px 26px rgba(0,0,0,.18)}
  .banner svg.backdrop{position:absolute;inset:0;width:100%;height:100%}
  .subject-photo{position:absolute;border-radius:22px 22px 0 0;
    background:linear-gradient(180deg,var(--kit-top) 0%,var(--kit-bottom) 100%);
    box-shadow:0 0 24px rgba(0,0,0,.25)}
  .club-mark{position:absolute;display:flex;align-items:center;gap:5px;
    font-family:"Montserrat",sans-serif;font-weight:800;color:var(--green-mid);
    line-height:1.1;text-transform:uppercase}
  .club-mark .dot{flex:none;border-radius:50%;background:var(--green-mid)}
  .name{position:absolute;transform:translateX(-50%);text-align:center;
    font-family:"Bebas Neue",sans-serif;line-height:1;white-space:nowrap;color:var(--white)}
  .name .first{display:block;text-shadow:0 3px 10px rgba(0,0,0,.45)}
  .name .last{display:block;text-shadow:0 6px 18px rgba(0,0,0,.5)}
  .name .accent{color:var(--lime)}
  .club-tag{position:absolute;display:flex;align-items:center;justify-content:center;
    background:var(--white);clip-path:polygon(0 0,100% 0,92% 100%,8% 100%);
    font-family:"Montserrat",sans-serif;font-weight:700;color:var(--blue);
    text-transform:uppercase;white-space:nowrap}
</style>
</head>
<body>
<div class="sheet">

  <div class="platform-label" style="top:22px">TWITTER BANNER</div>
  <section class="banner banner--twitter" style="left:96px;top:66px;width:856px;height:285px">
    <svg class="backdrop" viewBox="0 0 856 285" preserveAspectRatio="none">
      <defs>
        <linearGradient id="tw-bg" x1="0" y1="1" x2="1" y2="0">
          <stop offset="0" stop-color="#03602e"/><stop offset=".5" stop-color="#077a42"/><stop offset="1" stop-color="#03602e"/>
        </linearGradient>
      </defs>
      <rect width="856" height="285" fill="url(#tw-bg)"/>
      <circle cx="176" cy="147" r="138" fill="#ffffff" opacity=".07"/>
      <polygon points="0,0 141,0 83,95 0,95" fill="#fff"/>
      <polygon points="419,285 434,285 719,0 704,0" fill="#fff"/>
      <polygon points="467,285 747,0 856,0 856,80 652,285" fill="#fff"/>
      <polygon points="825,187 856,153 856,166 837,187" fill="#fff"/>
    </svg>
    <div class="subject-photo" role="img" aria-label="Photo of coach Dorian Halvorsen pointing, in a dark training jacket"
      style="left:560px;top:8px;width:270px;height:277px"></div>
    <div class="club-mark" style="left:10px;top:30px;width:80px;font-size:10px">
      <span class="dot" style="width:12px;height:12px"></span><span>Tuvo Rembeka FC</span>
    </div>
    <div class="name" style="left:273px;top:58px">
      <span class="first" style="font-size:52px">Dorian</span>
      <span class="last" style="font-size:124px;margin-top:-4px"><span class="accent">Hal</span>vorsen</span>
    </div>
    <div class="club-tag" style="left:195px;top:214px;width:156px;height:22px;font-size:15px">Tuvo Rembeka</div>
  </section>

  <div class="platform-label" style="top:382px">FACEBOOK BANNER</div>
  <section class="banner banner--facebook" style="left:105px;top:423px;width:806px;height:354px">
    <svg class="backdrop" viewBox="0 0 806 354" preserveAspectRatio="none">
      <defs>
        <linearGradient id="fb-bg" x1="0" y1="1" x2="1" y2="0">
          <stop offset="0" stop-color="#03602e"/><stop offset=".45" stop-color="#066e39"/><stop offset="1" stop-color="#077a42"/>
        </linearGradient>
      </defs>
      <rect width="806" height="354" fill="url(#fb-bg)"/>
      <circle cx="239" cy="176" r="200" fill="#ffffff" opacity=".08"/>
      <polygon points="0,34 210,34 170,100 0,100" fill="#fff"/>
      <polygon points="280,354 294,354 647,0 633,0" fill="#fff"/>
      <polygon points="313,354 661,0 794,0 446,354" fill="#fff"/>
      <polygon points="474,354 806,21 806,35 488,354" fill="#fff"/>
    </svg>
    <div class="subject-photo" role="img" aria-label="Photo of coach Dorian Halvorsen pointing, in a dark training jacket"
      style="left:470px;top:55px;width:208px;height:299px"></div>
    <div class="club-mark" style="left:124px;top:50px;width:70px;font-size:8px">
      <span class="dot" style="width:10px;height:10px"></span><span>Tuvo Rembeka FC</span>
    </div>
    <div class="name" style="left:279px;top:93px">
      <span class="first" style="font-size:35px">Dorian</span>
      <span class="last" style="font-size:82px;margin-top:-3px"><span class="accent">Hal</span>vorsen</span>
    </div>
    <div class="club-tag" style="left:221px;top:203px;width:116px;height:16px;font-size:11px">Tuvo Rembeka</div>
  </section>

  <div class="platform-label" style="top:796px">LINKEDIN BANNER</div>
  <section class="banner banner--linkedin" style="left:56px;top:840px;width:904px;height:227px">
    <svg class="backdrop" viewBox="0 0 904 227" preserveAspectRatio="none">
      <defs>
        <linearGradient id="li-bg" x1="0" y1="1" x2="1" y2="0">
          <stop offset="0" stop-color="#03602e"/><stop offset=".5" stop-color="#077a42"/><stop offset="1" stop-color="#03602e"/>
        </linearGradient>
      </defs>
      <rect width="904" height="227" fill="url(#li-bg)"/>
      <circle cx="215" cy="105" r="127" fill="#ffffff" opacity=".07"/>
      <polygon points="0,0 143,0 95,82 0,82" fill="#fff"/>
      <polygon points="488,227 502,227 724,0 710,0" fill="#fff"/>
      <polygon points="535,227 757,0 904,0 904,41 688,227" fill="#fff"/>
      <polygon points="823,191 904,108 904,122 837,191" fill="#fff"/>
    </svg>
    <div class="subject-photo" role="img" aria-label="Photo of coach Dorian Halvorsen pointing, in a dark training jacket"
      style="left:575px;top:4px;width:247px;height:223px"></div>
    <div class="club-mark" style="left:24px;top:24px;width:80px;font-size:10px">
      <span class="dot" style="width:12px;height:12px"></span><span>Tuvo Rembeka FC</span>
    </div>
    <div class="name" style="left:313px;top:30px">
      <span class="first" style="font-size:52px">Dorian</span>
      <span class="last" style="font-size:122px;margin-top:-4px"><span class="accent">Hal</span>vorsen</span>
    </div>
    <div class="club-tag" style="left:227px;top:187px;width:156px;height:22px;font-size:15px">Tuvo Rembeka</div>
  </section>

</div>
</body>
</html>
```